ATTORNEY FULL PAGE AD

We need a full page flyer for our law firm. We are sending it to people who were in an auto accident and injured. I want to let people know that by hiring an attorney that does not mean that they are suing someone. We will just help them in filing a claim and to get them compensated for: medical bills, lost wages, car repairs, future medical treatment or surgery, and pain/suffering. They will NOT have to pay us any money unless we get them paid. I want to show that we are compassionate to the fact that they went through this tramatic event that will effect their lives for ever. They do not have to worry about anything once they hire us. Our website is: www.brightwelllawfirm.com Our colors are black and gold. NO GAMBLING REFERENCES!!!!
Updates

Don't worry so much about content and wording. Once we get a design and images that look great we will message you the exact words we would like put into the paragraphs. The overall "look" and images are the most important. If anyone has a great change-up logo we are open to it as well. Thanks for everyone's hard work!

We like the dark colors. Some of the images are a little cheesy. We are a family business and treat are clients as family. I like the pictures o the car crashes an the hands. No blood. We want to come off as respectful and trustworthy. It's more about how we will care for them as family than getting them lots of money. 

Target Market(s)

People who were in major accidents and have serious injuries

Industry/Entity Type

Attorney

Requirements
Must have
• Must have our phone number: 1-855-MBRIGHT
Website: www.brightwelllawfirm.com
Company name: Brightwell Law Group
Attorney name: Morgan Ellis Brightwell
High gloss with card stock paper.
Classy - NOT cheesy
Should not have
• No cartoons. Very masculine and professional. There may have been death involved in the accident so we want the ad to be very compassionate and moving.

```html
<!DOCTYPE html>
<html lang="en">
<head>
<meta charset="utf-8">
<title>Brightwell Law Group – Auto Accident Flyer</title>
<link rel="stylesheet" href="https://fonts.googleapis.com/css2?family=Alfa+Slab+One&family=Arimo:wght@400;700&family=Roboto+Slab:wght@800&display=swap">
<style>
  :root {
    --page-bg: #efefef;
    --asphalt-light: #6a6a6a;
    --asphalt-mid: #555555;
    --asphalt-dark: #3f3f3f;
    --headline-white: #f4f4f2;
    --body-white: #ffffff;
    --accent-red: #c8121f;
    --frame-line: #2a2a2a;
  }
  html, body {
    margin: 0;
    width: 1200px;
    height: 800px;
    overflow: hidden;
    background: var(--page-bg);
  }
  .flyer {
    position: absolute;
    left: 295px;
    top: 24px;
    width: 600px;
    height: 752px;
  }
  .headline {
    font-family: "Alfa Slab One", "Roboto Slab", serif;
    fill: var(--headline-white);
  }
  .subhead {
    font-family: "Arimo", Arial, sans-serif;
    font-weight: 400;
    fill: var(--body-white);
  }
  .phone {
    font-family: "Roboto Slab", "Alfa Slab One", serif;
    font-weight: 800;
    fill: var(--accent-red);
  }
  .website, .firm-name {
    font-family: "Arimo", Arial, sans-serif;
    font-weight: 700;
    fill: var(--body-white);
  }
</style>
</head>
<body>
<svg class="flyer" viewBox="0 0 600 752" xmlns="http://www.w3.org/2000/svg">
  <defs>
    <radialGradient id="asphaltTone" cx="45%" cy="40%" r="80%">
      <stop offset="0%" stop-color="var(--asphalt-light)"/>
      <stop offset="60%" stop-color="var(--asphalt-mid)"/>
      <stop offset="100%" stop-color="var(--asphalt-dark)"/>
    </radialGradient>
  </defs>

  <rect class="asphalt-photo" x="0" y="0" width="600" height="752" fill="url(#asphaltTone)"
        role="img" aria-label="Photograph of asphalt road with a skid mark and scattered broken glass"/>
  <rect class="flyer-frame" x="0.5" y="0.5" width="599" height="751" fill="none" stroke="var(--frame-line)" stroke-width="1"/>

  <g class="headline" font-size="104">
    <text x="80" y="146">I</text>
    <text x="80" y="235" textLength="370" lengthAdjust="spacingAndGlyphs">DON'T</text>
    <text x="80" y="321" textLength="370" lengthAdjust="spacingAndGlyphs">KNOW</text>
    <text x="80" y="407" textLength="415" lengthAdjust="spacingAndGlyphs">I HAVE</text>
    <text x="80" y="496" textLength="435" lengthAdjust="spacingAndGlyphs">RIGHTS</text>
  </g>

  <g class="subhead" font-size="21">
    <text x="88" y="549" textLength="414" lengthAdjust="spacingAndGlyphs">GET HELP AND BE COMPENSATED</text>
    <text x="88" y="581" textLength="170" lengthAdjust="spacingAndGlyphs">IN AUTO ACCIDENT</text>
  </g>

  <text class="phone" x="86" y="630" font-size="42" textLength="424" lengthAdjust="spacingAndGlyphs">1-855-MBRIGHT</text>

  <text class="website" x="88" y="663" font-size="17" textLength="412" lengthAdjust="spacing">www.brightwelllawfirm.com</text>

  <text class="firm-name" x="88" y="694" font-size="16" textLength="392" lengthAdjust="spacingAndGlyphs">Brightwell Law Group / Morgan Ellis Brightwell</text>
</svg>
</body>
</html>
```